Coaching company requires a Bi-Fold Services Brochure

**Please also read attached design brief***

As part of our expanding sales role for our Professional Development Company, we need a Bi-Fold services brochure that offers our clients some further information about our specific services.

This services brochure will be the document that our clients will receive after our initial contact with them so the overall design of this document will play an instrumental part in our securing of ongoing work.

We have prepared a design brief for designers that want to undertake this task and this document should help to clarify any missing information from this online brief. Any designer who is interested in submitting a design should also refer to this attached document to get the full scope of the works required.

Regular email correspondence will also be available to clarify any questions that the design may have

*** Please also note that the finished design will need to be submitted in a PSD format to allow for editing in Photoshop CS6

Target Market(s)

Our target market is Business to Business. We are specifically targeting small, medium and large businesses who are looking to invest in Professional Development for their business and their staff.
The areas of major focus are 1 on 1 coaching of leaders, executives & business owners and group facilitation sessions with their staff.

Industry/Entity Type

Business Service

Font styles to use
Sans Serif

Requirements
Must have
• - Design needs to be an A4 Bi-Fold layout so should suit an A3 sheet of paper (297mm x 420mm)
• - Include our corporate color scheme
• - Finished design must be in PSD format or format that can be edited in Photshop CS6
• - Appealing to small, medium and large businesses (universal appeal)
• - The project must be in CMYK Colour and no less than 300 pixel resolution
Nice to have
• - Our logo incorporated into the front page
• - We would like the images used in this brochure to be happy and vibrant (i.e. smiling faces and energetic etc.)

```html
<!DOCTYPE html>
<html lang="en">
<head>
<meta charset="utf-8">
<title>Meridian PD – Services Brochure</title>
<link rel="stylesheet" href="https://fonts.googleapis.com/css2?family=Lato:wght@400;700&family=Questrial&display=swap">
<style>
  :root {
    --blue: #1a8ad8;
    --blue-deep: #0b6fc0;
    --ink: #1f1f1f;
    --black: #111111;
    --charcoal: #2c2d30;
    --grey-light: #eef0f2;
    --grey-mid: #b9bdc2;
    --white: #ffffff;
    --backdrop: #e4e4e4;
  }
  * { margin: 0; padding: 0; box-sizing: border-box; }
  html, body { width: 1200px; height: 907px; overflow: hidden; background: var(--backdrop); }
  .canvas { position: relative; width: 1200px; height: 907px; }
  .spread {
    position: absolute; left: 90px; top: 90px; width: 1020px; height: 728px;
    background: var(--white); overflow: hidden;
    box-shadow: 0 6px 24px rgba(0,0,0,.25);
  }
  .spread-art { position: absolute; inset: 0; }

  /* left page */
  .inside-page { position: absolute; left: 0; top: 0; width: 508px; height: 728px; }
  .page-title {
    position: absolute; left: 20px; top: 22px;
    font: 700 24px "Questrial", sans-serif; color: var(--blue); letter-spacing: .2px;
  }
  .testimonial { position: absolute; left: 20px; width: 468px; }
  .testimonial .quote {
    font: 400 9.4px/11.6px "Lato", sans-serif; color: var(--ink); text-align: justify;
  }
  .testimonial .quote + .quote { margin-top: 4px; }
  .mark { color: var(--blue); font: 700 22px/0 "Lato", sans-serif; vertical-align: -7px; }
  .mark.open { margin-right: 2px; }
  .mark.close { margin-left: 3px; }
  .author { margin: 10px 0 0 97px; font: 400 12px/14px "Lato", sans-serif; color: var(--ink); }
  .author .name { font: 700 15px/17px "Questrial", sans-serif; color: var(--blue); }

  .contact-row {
    position: absolute; left: 30px; top: 695px; display: flex; gap: 26px;
    font: 400 12px "Lato", sans-serif; color: var(--white);
  }
  .contact-row span { display: flex; align-items: center; gap: 6px; }

  /* cover page */
  .cover-page { position: absolute; left: 508px; top: 0; width: 512px; height: 728px; }
  .brand {
    position: absolute; left: 0; right: 0; top: 46px;
    display: flex; justify-content: center; align-items: center; gap: 14px;
    font: 400 36px "Questrial", sans-serif; color: var(--white); letter-spacing: 2px;
  }
  .brand .dot { width: 34px; height: 34px; border-radius: 50%; background: var(--white); }
  .team-photo {
    position: absolute; left: 52px; top: 114px; width: 416px; height: 416px; border-radius: 50%;
    background: radial-gradient(circle at 50% 40%, #f4f4f2 0%, #d9d6d0 45%, #3a3a3e 75%, #c9b79c 100%);
  }
  .cover-title {
    position: absolute; left: 0; right: 0; top: 570px; text-align: center;
    font: 400 36px "Questrial", sans-serif; color: var(--ink);
  }
  .cover-title .accent { color: var(--blue); font-weight: 700; }
  .cover-web {
    position: absolute; left: 0; right: 0; top: 692px; text-align: center;
    font: 700 16px "Lato", sans-serif; color: var(--white); letter-spacing: 6px;
  }
</style>
</head>
<body>
<div class="canvas">
  <div class="spread">
    <svg class="spread-art" width="1020" height="728" viewBox="0 0 1020 728" aria-hidden="true">
      <defs>
        <linearGradient id="coverBlue" x1="0" y1="0" x2="0" y2="1">
          <stop offset="0" stop-color="#1a8ad8"/><stop offset="1" stop-color="#0b6fc0"/>
        </linearGradient>
        <linearGradient id="coverGrey" x1="0" y1="0" x2="1" y2="1">
          <stop offset="0" stop-color="#a9adb2"/><stop offset=".45" stop-color="#f1f2f3"/><stop offset="1" stop-color="#9ea2a7"/>
        </linearGradient>
        <linearGradient id="cityFade" x1="0" y1="0" x2="1" y2="1">
          <stop offset="0" stop-color="#ffffff" stop-opacity="0"/><stop offset=".6" stop-color="#c9d3dc" stop-opacity=".45"/><stop offset="1" stop-color="#9fb0c0" stop-opacity=".55"/>
        </linearGradient>
      </defs>
      <!-- left page backdrop -->
      <rect x="0" y="0" width="508" height="728" fill="#ffffff"/>
      <rect x="0" y="220" width="508" height="470" fill="url(#cityFade)" role="img" aria-label="Faint photo of office towers"/>
      <path d="M0,548 Q254,756 508,590" fill="none" stroke="#1a8ad8" stroke-width="3"/>
      <path d="M0,562 Q254,770 508,606 L508,728 L0,728 Z" fill="#111111"/>
      <!-- cover backdrop -->
      <rect x="508" y="0" width="512" height="265" fill="url(#coverBlue)"/>
      <rect x="508" y="265" width="512" height="463" fill="url(#coverGrey)"/>
      <line x1="527" y1="26" x2="527" y2="26" stroke="none"/>
      <circle cx="768" cy="322" r="232" fill="#2c2d30"/>
      <path d="M1000,322 A232,232 0 0 1 536,322" fill="none" stroke="#1a8ad8" stroke-width="12"/>
      <circle cx="768" cy="322" r="216" fill="#ffffff"/>
      <path d="M508,598 Q765,749 1020,590" fill="none" stroke="#1a8ad8" stroke-width="3"/>
      <path d="M508,618 Q765,770 1020,608 L1020,728 L508,728 Z" fill="#111111"/>
    </svg>

    <section class="inside-page">
      <h2 class="page-title">Testimonials</h2>

      <article class="testimonial" style="top:58px">
        <p class="quote"><span class="mark open">“</span>Our company has worked closely with Graham over the past 24 months. In that time he has taken a detailed, professional, caring approach to developing our leaders as individuals and as a team. Graham is one of those extraordinary individuals who takes the time to understand the true needs of our emerging leaders. His astuteness and professionalism have enabled our leadership team to grasp the fundamentals of life and that of business responsibilities. Graham's personalized care has been the cornerstone to building character and resilience in our staff.</p>
        <p class="quote">He has an exceptional strength in relating our cultural values to the personal purposes of our employees. To this end Graham is motivated to find the element that bring out the best in a person and capture the appealing factors that make our people tick. This all leads to building a resilient team of accomplished people who are energetic and driven. He is an invaluable partner to our business and key to the future success of our company. I would highly recommend Graham to anyone who's looking to enhance their people and the performance of their business<span class="mark close">”</span></p>
        <div class="author"><div class="name">Oliver</div>Business Owner &amp; Managing Director<br>Construction Industry</div>
      </article>

      <article class="testimonial" style="top:262px">
        <p class="quote"><span class="mark open">“</span>In less than 6 months working with Graham from Meridian, I have raised my team's game to a whole new level and have learned to delegate more effectively. My relationships with peers, direct reports and key decision-makers have improved greatly, making me a more confident leader. After each session I always walk away with a new, clear, perspective on how to approach my work challenges and a very clear plan of attack. I would strongly recommend Meridian to anyone who is looking to take their leadership to the next level<span class="mark close">”</span></p>
        <div class="author"><div class="name">Tessa</div>Finance Manager<br>Construction Industry</div>
      </article>

      <article class="testimonial" style="top:374px">
        <p class="quote"><span class="mark open">“</span>I have found in the past that most professional coaches only provide fluffy solutions to the issues that make you feel good in the short term. Unlike Graham who helped me to identify the issues I was facing that I could not pin point on my own. Even after pin pointing the issues, he provided me with the right tools and knowledge that I required to work through the problems and achieve the results I was after.<span class="mark close">”</span></p>
        <div class="author"><div class="name">Rob</div>Operations Manager<br>Construction Industry</div>
      </article>

      <article class="testimonial" style="top:480px">
        <p class="quote"><span class="mark open">“</span>I have engaged Graham on several occasions to assist me with the immediate needs and the future development of my business. At first I was a little skeptical as to what, if anything, Graham would be able to help us with. Immediately he put my mind at ease by proving himself to be both exceptionally capable and highly professional. Graham produced some very impressive results that assisted us to fulfil our immediate business needs as well as being able to identify some areas of focus in moving our business forward. Graham has a very unique way of explaining complex business strategy and in putting it into easy to understand and easy to apply actions. After working closely with Graham for the past year, I have no problem in engaging him on a long term relationship to help develop and build my business for the future.<span class="mark close">”</span></p>
        <div class="author" style="color:var(--ink)"><div class="name">Conrad</div>Business Owner<br>Managing Director</div>
      </article>

      <div class="contact-row">
        <span><svg width="11" height="11" viewBox="0 0 11 11" aria-hidden="true"><rect width="11" height="11" rx="2" fill="#1a8ad8"/><path d="M3,2.5 L4.4,2.5 L5,4.2 L4.2,4.9 Q5,6.3 6.2,6.8 L6.9,6 L8.5,6.6 L8.5,8 Q4,8.5 3,2.5Z" fill="#fff"/></svg>(03) 55 204417</span>
        <span><svg width="12" height="9" viewBox="0 0 12 9" aria-hidden="true"><rect width="12" height="9" rx="1" fill="#1a8ad8"/><path d="M0.5,0.8 L6,5 L11.5,0.8" fill="none" stroke="#fff" stroke-width="1"/></svg>hello@meridianpd.com.au</span>
        <span><svg width="11" height="11" viewBox="0 0 11 11" aria-hidden="true"><circle cx="5.5" cy="5.5" r="5" fill="#1a8ad8"/><ellipse cx="5.5" cy="5.5" rx="2.2" ry="5" fill="none" stroke="#fff" stroke-width=".7"/><line x1=".5" y1="5.5" x2="10.5" y2="5.5" stroke="#fff" stroke-width=".7"/></svg>www.meridianpd.com.au</span>
      </div>
    </section>

    <section class="cover-page">
      <div class="brand"><span class="dot"></span>MERIDIAN PD</div>
      <div class="team-photo" role="img" aria-label="Photo of a smiling business team gathered around a meeting table with a laptop"></div>
      <h1 class="cover-title"><span class="accent">Services</span> Brochure</h1>
      <div class="cover-web">www.meridianpd.com.au</div>
    </section>
  </div>
</div>
</body>
</html>
```